Business Card Design

I need a business card for a new company based in Australia called "MedLinkora".

Its a cloud program for GPs that allows them to search for the specialist they require using a simple user friendly tool.

I would like the colours to match those in the program (the colours in the logo attached).

The final design should reflect the programs clarity, ease of use and professionalism.

Target Market(s)

GPs and other Health Professionals

Industry/Entity Type

Business

Contact Information for Business Card

MedLinkora; The Trusted Clinician Index; Marla Ostrove CEO; 0438215906; marla@medlinkora.example; www.medlinkora.example

Requirements
Must have
• Must have the logo attached; the web address and my name and phone number
Nice to have
• the slogan "The Trusted Clinician Index"

```html
<!DOCTYPE html>
<html lang="en">
<head>
<meta charset="utf-8">
<title>MedLinkora Business Card</title>
<link rel="stylesheet" href="https://fonts.googleapis.com/css2?family=Arimo:wght@400&display=swap">
<style>
  :root {
    --page-bg: #eeeff1;
    --brand-blue: #13b0e6;
    --soft-blue: #8fd1ef;
    --ink-grey: #8a8a8a;
    --band-grey-dark: #b3b3b3;
    --band-grey-light: #ececec;
    --card-white: #ffffff;
  }
  html, body {
    margin: 0;
    width: 1200px;
    height: 1000px;
    overflow: hidden;
    background: var(--page-bg);
  }
  .canvas {
    position: relative;
    width: 1200px;
    height: 1000px;
  }
  .card {
    position: absolute;
    display: block;
    box-shadow: 0 2px 8px rgba(0,0,0,0.18);
  }
  .card--front { left: 15px; top: 15px; }
  .card--back { left: 403px; top: 503px; }
  .brand-name, .brand-tagline, .person-name, .person-role, .contact-line {
    font-family: "Arimo", sans-serif;
    font-weight: 400;
  }
  .brand-name, .person-name, .contact-line { fill: var(--brand-blue); }
  .brand-mark { fill: var(--brand-blue); }
  .brand-tagline, .person-role { fill: var(--ink-grey); }
</style>
</head>
<body>
<main class="canvas">

  <svg class="card card--front" width="777" height="470" viewBox="0 0 777 470" aria-label="Business card front">
    <defs>
      <linearGradient id="front-grey" x1="0" y1="0" x2="0" y2="1">
        <stop offset="0" stop-color="var(--band-grey-light)"/>
        <stop offset="1" stop-color="var(--band-grey-dark)"/>
      </linearGradient>
      <linearGradient id="front-blue" x1="0" y1="0" x2="0" y2="1">
        <stop offset="0.35" stop-color="var(--brand-blue)"/>
        <stop offset="1" stop-color="var(--card-white)"/>
      </linearGradient>
    </defs>
    <rect class="card-base" width="777" height="470" fill="var(--card-white)"/>
    <path class="band-top" d="M0 0 H777 V170 Q388 -10 0 170 Z" fill="url(#front-grey)"/>
    <path class="band-bottom" d="M0 335 Q388 490 777 320 V470 H0 Z" fill="url(#front-blue)"/>
    <rect class="brand-mark" x="96" y="190" width="44" height="44"/>
    <text class="brand-name" x="160" y="264" font-size="96">MedLinkora</text>
    <text class="brand-tagline" x="388" y="314" text-anchor="middle" font-size="36">The Trusted Clinician Index</text>
  </svg>

  <svg class="card card--back" width="778" height="470" viewBox="0 0 778 470" aria-label="Business card back">
    <defs>
      <linearGradient id="back-grey" x1="0" y1="0" x2="0" y2="1">
        <stop offset="0" stop-color="var(--card-white)"/>
        <stop offset="1" stop-color="var(--band-grey-dark)"/>
      </linearGradient>
      <linearGradient id="back-blue" x1="0" y1="0" x2="0" y2="1">
        <stop offset="0.3" stop-color="var(--soft-blue)"/>
        <stop offset="1" stop-color="var(--card-white)"/>
      </linearGradient>
    </defs>
    <rect class="card-base" width="778" height="470" fill="var(--card-white)"/>
    <path class="band-top" d="M0 0 H778 V180 Q420 -20 0 130 Z" fill="url(#back-grey)"/>
    <path class="band-bottom" d="M0 325 Q390 470 778 310 V470 H0 Z" fill="url(#back-blue)"/>
    <rect class="brand-mark" x="22" y="37" width="36" height="36"/>
    <text class="brand-name" x="70" y="75" font-size="52">MedLinkora</text>
    <text class="brand-tagline" x="22" y="112" font-size="25">The Trusted Clinician Index</text>
    <text class="person-name" x="21" y="218" font-size="37">Marla Ostrove</text>
    <text class="person-role" x="21" y="240" font-size="21">CEO</text>
    <text class="contact-line" x="378" y="344" text-anchor="middle" font-size="18">Phone:0438215906</text>
    <text class="contact-line" x="378" y="368" text-anchor="middle" font-size="18">Web:www.medlinkora.example</text>
    <text class="contact-line" x="378" y="392" text-anchor="middle" font-size="18">Email:marla@medlinkora.example</text>
  </svg>

</main>
</body>
</html>
```